Pinecrest Premier Motors *

Professional business cards for our auto wholesale dealership.

Target Market(s)

New and used cars sales managers and middle class to higher end private party buyers.

Industry/Entity Type

Automotive

Contact Information for Business Card

Pinecrest Premier Motors
Marcus T Holloran
Owner
(555) 014-3862
pineprem@mailvista.example
Dealer Lic # 48265

Logo Text

Pinecrest Premier Motors, Pine Prem Motors, PPM, etc

Font styles to use
Serif
Sans Serif

Colors

Designer to choose colors to be used in the design.

Requirements
Must have
• A professional, but not pretentious, look
Nice to have
• It might be nice to see "PPM" in a shape form i.e. circle, triangle, etc in the corner or background somehwere
Should not have
• bright "girly" colors

```html
<!DOCTYPE html>
<html lang="en">
<head>
<meta charset="utf-8">
<title>Pinecrest Premier Motors — Business Card</title>
<link href="https://fonts.googleapis.com/css2?family=Montserrat:wght@400;600&display=swap" rel="stylesheet">
<style>
  :root {
    --backdrop: #c3c3c3;
    --teal: #016779;
    --logo-muted: #8fa3ad;
    --paper-light: #f4f5f5;
    --paper-mid: #d9dbdb;
    --paper-dark: #b9bcbd;
    --ink-light: #ffffff;
  }
  * { margin: 0; padding: 0; box-sizing: border-box; }
  html, body {
    width: 1200px;
    height: 1200px;
    overflow: hidden;
    background: var(--backdrop);
    font-family: "Montserrat", sans-serif;
  }
  .canvas {
    position: relative;
    width: 1200px;
    height: 1200px;
  }
  .card {
    position: absolute;
    left: 322px;
    width: 538px;
    height: 308px;
    box-shadow: 2px 3px 4px rgba(0, 0, 0, 0.35);
    overflow: hidden;
  }
  .card-front {
    top: 178px;
    background: var(--teal);
    color: var(--ink-light);
  }
  .card-back {
    top: 633px;
  }
  .holder {
    position: absolute;
    left: 37px;
    top: 50px;
    display: flex;
    align-items: center;
    white-space: nowrap;
  }
  .holder-name {
    font-size: 20px;
    font-weight: 400;
  }
  .holder-divider {
    width: 1px;
    height: 20px;
    background: var(--ink-light);
    margin: 0 13px 0 12px;
  }
  .holder-title {
    font-size: 13px;
    font-weight: 400;
    letter-spacing: 0.3px;
    padding-top: 3px;
  }
  .wordmark {
    position: absolute;
    font-weight: 600;
    line-height: 1;
    letter-spacing: 1px;
    white-space: nowrap;
  }
  .card-front .wordmark {
    left: 35px;
    top: 212px;
    font-size: 72px;
    color: var(--logo-muted);
  }
  .contact {
    position: absolute;
    left: 297px;
    top: 185px;
    font-size: 14.5px;
    line-height: 22.5px;
    white-space: nowrap;
  }
  .contact-license {
    margin-top: 20px;
  }
  .back-surface {
    position: absolute;
    inset: 0;
    background:
      linear-gradient(160deg, var(--paper-mid) 0%, var(--paper-light) 30%, #ffffff 55%, var(--paper-mid) 80%, var(--paper-dark) 100%);
  }
  .card-back .wordmark {
    left: 0;
    right: 0;
    top: 100px;
    text-align: center;
    font-size: 118px;
    color: var(--teal);
  }
</style>
</head>
<body>
<main class="canvas">
  <section class="card card-front" aria-label="Business card front">
    <div class="holder">
      <span class="holder-name">Marcus T Holloran</span>
      <span class="holder-divider"></span>
      <span class="holder-title">Owner</span>
    </div>
    <div class="wordmark">PPM</div>
    <div class="contact">
      <p>P: (555) 014-3862</p>
      <p>E: pineprem@mailvista.example</p>
      <p class="contact-license">Dealer Lic # 48265</p>
    </div>
  </section>

  <section class="card card-back" aria-label="Business card back">
    <div class="back-surface" role="img" aria-label="Light grey faceted low-poly background pattern"></div>
    <div class="wordmark">PPM</div>
  </section>
</main>
</body>
</html>
```